TRB Fitouts

Kitchen installations/ carpentry / labour hire

Target Market(s)

Building companys

Industry/Entity Type

Carpentry

Contact Information for Business Card

Director Tadhg Brennock
Phone no 0478215096
Email tadhgbrennock@trbfitouts.example.com.au

Requirements
Nice to have
• A finished kitchen on one side in the background I would like my company name in big writing and my name in small writing so on one side I would like trb fitouts and on the other side have my details with the picture of the kitchen in the back round
Should not have
• Fork and spoons

```html
<!DOCTYPE html>
<html lang="en">
<head>
<meta charset="utf-8">
<title>TRB Fitouts – Business Card</title>
<link rel="stylesheet" href="https://fonts.googleapis.com/css2?family=Cinzel:wght@400;600&family=PT+Sans:wght@400&display=swap">
<style>
  :root {
    --backdrop: #3a3a3c;
    --paper: #f4f4f4;
    --teal: #1f9596;
    --teal-deep: #1b8f97;
    --green: #7aae32;
    --ink: #2b2b2b;
    --rule: #b9b9b9;
  }
  * { box-sizing: border-box; margin: 0; padding: 0; }
  html, body {
    width: 1200px; height: 896px; overflow: hidden;
    background: var(--backdrop);
  }
  .sheet {
    width: 1200px; height: 896px;
    display: flex; flex-direction: column; align-items: center; justify-content: center;
    gap: 40px;
  }
  .card {
    position: relative;
    width: 700px; height: 400px;
    overflow: hidden;
    box-shadow: 0 10px 24px rgba(0,0,0,.45);
  }
  /* Front */
  .card--front { background: var(--paper); }
  .contact {
    position: absolute; left: 48px; top: 110px;
    font-family: "PT Sans", sans-serif; color: var(--ink);
  }
  .contact__name {
    font-family: "Cinzel", serif; font-weight: 400;
    font-size: 24px; letter-spacing: 1px; color: var(--teal);
  }
  .contact__name .surname { color: var(--green); }
  .contact__role { font-size: 18px; margin: 2px 0 22px; }
  .contact__line {
    display: flex; align-items: center; gap: 8px;
    font-size: 18px; line-height: 26px;
  }
  .contact__line svg { width: 16px; height: 16px; fill: var(--teal); }
  .wordmark {
    position: absolute; right: 60px; top: 150px;
    font-family: "Cinzel", serif; font-weight: 600;
    font-size: 54px; color: var(--teal); letter-spacing: 2px;
  }
  .divider {
    position: absolute; left: 48px; right: 48px; top: 292px;
    height: 1px; background: var(--rule);
  }
  .address {
    position: absolute; right: 60px; top: 306px; text-align: right;
    font-family: "PT Sans", sans-serif; font-size: 18px; line-height: 24px; color: var(--ink);
  }
  .edge {
    position: absolute; left: 0; right: 0; bottom: 0; height: 12px;
    background: linear-gradient(90deg, var(--teal) 0 40%, var(--green) 40% 100%);
  }
  /* Back */
  .card--back {
    background: linear-gradient(160deg, var(--green) 0%, #4ea25a 45%, var(--teal-deep) 100%);
    display: flex; align-items: center; justify-content: center;
  }
  .card--back .wordmark--light {
    font-family: "Cinzel", serif; font-weight: 600;
    font-size: 64px; color: #ffffff; letter-spacing: 2px;
  }
</style>
</head>
<body>
<main class="sheet">
  <section class="card card--front" aria-label="Business card front">
    <div class="contact">
      <p class="contact__name">Liam <span class="surname">Corrigan</span></p>
      <p class="contact__role">Managing Director</p>
      <p class="contact__line">
        <svg viewBox="0 0 16 16" aria-hidden="true"><path d="M2 5c0-2 2-3 6-3s6 1 6 3v1h-3V5H5v1H2zM4 7h8l2 6H2z"/></svg>
        044-987 612 345
      </p>
      <p class="contact__line">
        <svg viewBox="0 0 16 16" aria-hidden="true"><path d="M4 1h8v14H4zM5.5 3v9h5V3z"/></svg>
        044-987 612 345
      </p>
      <p class="contact__line">
        <svg viewBox="0 0 16 16" aria-hidden="true"><path d="M1 3h14v10H1zM2.5 4.5 8 9l5.5-4.5z"/></svg>
        info@trbfitouts.example.com
      </p>
    </div>
    <p class="wordmark">TRB Fitouts</p>
    <div class="divider"></div>
    <p class="address">12345, Address Goes Here<br>Country Name, 123456</p>
    <div class="edge"></div>
  </section>

  <section class="card card--back" aria-label="Business card back">
    <p class="wordmark--light">TRB Fitouts</p>
  </section>
</main>
</body>
</html>
```